Webdesign für Verkauf von Stoffen
Zielgruppe
Palmtuche ist schon seit 15 Jahren auf den Märkten unterwegs und verkauft seine hochwertigen Stoffe vor Ort. Nun muss die Webseite ein neuen Look bekommen, sie sollte modern und locker wirken. Die Webseite ist eher für Privatkunden und hat jetzt noch keine Shop Möglichkeit, die wird aber intrigiert mit einzelnen Produkten.
Aufgabenstellung
Logo gibt es noch nicht, soll erstmal nur in Schriftform bleiben, ansonsten gibt es keine explizierten Vorgaben

```html
<!DOCTYPE html>
<html lang="de">
<head>
<meta charset="utf-8">
<title>Palmtuche - Sonnenfaden</title>
<link href="https://fonts.googleapis.com/css2?family=Lato:wght@400;700&display=swap" rel="stylesheet">
<style>
:root{
  --brand:#6f95d9;
  --brand-dark:#5a80c6;
  --ink:#1f1f1f;
  --muted:#555;
  --light:#f5f5f5;
  --white:#fff;
}
*{margin:0;padding:0;box-sizing:border-box}
html,body{width:1200px;height:2992px;overflow:hidden;background:var(--white);font-family:'Lato',sans-serif;color:var(--ink)}
.page{position:relative;width:1200px;height:2992px}
.abs{position:absolute}

.topbar{left:0;top:0;width:1200px;height:50px;background:var(--brand);color:var(--white);z-index:2}
.wordmark{left:40px;top:15px;font-size:17px;font-weight:400}
.wordmark b{font-weight:700}
.nav{left:460px;top:17px;display:flex;gap:21px;font-size:13px}
.nav .active{font-weight:700}
.usernav{right:40px;top:17px;display:flex;gap:20px;font-size:11px;align-items:center}
.usernav span{display:flex;align-items:center;gap:8px}

.hero{left:0;top:50px;width:1200px;height:596px;background:linear-gradient(180deg,#4e5574 0%,#5b6a92 45%,#6b7aa0 100%)}
.hero-shade{left:0;top:50px;width:1200px;height:596px;background:rgba(20,30,70,.35)}
.hero-dots{left:295px;top:277px;display:flex;gap:6px}
.hero-dots i{display:block;width:16px;height:2px;background:var(--white)}
.hero-dots i:first-child{background:var(--brand)}
.hero-title{left:295px;top:298px;font-size:28px;font-weight:700;color:var(--white)}
.hero-text{left:295px;top:343px;font-size:13px;color:var(--white)}
.btn{display:flex;align-items:center;justify-content:center;background:var(--brand);color:var(--white)}
.hero-btn{left:295px;top:386px;width:120px;height:32px;font-size:13px}

.features{left:0;top:646px;width:1200px;height:128px;background:var(--light)}
.feature{top:44px;display:flex;align-items:center;gap:12px;font-size:13px;color:var(--muted);line-height:17px}
.feature svg{width:44px;height:40px;fill:none;stroke:#666;stroke-width:1.6}

.section-title{left:0;width:1200px;text-align:center;top:867px;font-size:24px;font-weight:700}
.swatch{top:935px;width:100px;text-align:center}
.swatch .dot{width:100px;height:100px;border-radius:50%}
.swatch p{margin-top:13px;font-size:13px}
.more-btn{left:513px;top:1109px;width:174px;height:36px;font-size:14px;font-weight:700}

.banner{top:1260px;width:600px;height:479px}
.banner-label{bottom:52px;background:var(--white);font-size:24px;padding:10px 14px}

.product{top:1808px;width:217px}
.product .shot{width:217px;height:182px}
.product .tag{margin-top:12px;font-size:11px;color:var(--brand)}
.product h3{margin-top:6px;font-size:16px;font-weight:400;line-height:20px}
.product .price{margin-top:4px;font-size:11px}
.product .price small{color:#aaa;font-size:10px}

.about-title{left:135px;top:2270px;font-size:24px;font-weight:700}
.about-text{left:135px;top:2320px;width:350px;font-size:14px;line-height:20px;color:#333}
.about-photo{left:526px;top:2161px;width:540px;height:422px;background:linear-gradient(135deg,#e07a4d 0%,#d84a50 30%,#e2c24a 50%,#6f9aa3 75%,#efe7dc 100%)}

.footer{left:0;top:2729px;width:1200px;height:263px;background:var(--brand);color:var(--white)}
.f-col{top:52px}
.f-head{font-size:16px}
.f-list{margin-top:19px;font-size:14px;line-height:27px}
.f-brand{font-size:16px}
.f-brand b{font-weight:700}
.f-hot{margin-top:22px;font-size:14px}
.f-phone{margin-top:8px;font-size:20px;display:flex;align-items:center;gap:8px}
.f-hours{margin-top:6px;font-size:14px}
.social{margin-top:18px;display:flex;gap:12px;font-size:12px}
.social span{display:flex;align-items:center;gap:5px}
.social i{width:10px;height:10px;border-radius:50%;background:var(--white);display:block}
.pay{margin-top:16px;display:grid;grid-template-columns:84px 84px;gap:12px 8px;font-size:13px;font-weight:700}
.pay-rule{width:84px;height:1px;background:rgba(255,255,255,.6);margin:14px 0}
</style>
</head>
<body>
<div class="page">

  <header class="abs topbar">
    <div class="abs wordmark"><b>Palmtuche</b> - Sonnenfaden</div>
    <nav class="abs nav"><span class="active">Home</span><span>Shop</span><span>Kollekttionen</span><span>Über Uns</span></nav>
    <div class="abs usernav">
      <span>Shopping Cart
        <svg width="18" height="16" viewBox="0 0 18 16" fill="none" stroke="#fff" stroke-width="1.4"><path d="M1 1h3l2 9h9l2-6H5"/><circle cx="7" cy="14" r="1.3"/><circle cx="14" cy="14" r="1.3"/></svg>
      </span>
      <span>Account
        <svg width="16" height="16" viewBox="0 0 16 16" fill="none" stroke="#fff" stroke-width="1.4"><circle cx="8" cy="5" r="4"/><path d="M1 15c1-4 4-6 7-6s6 2 7 6"/></svg>
      </span>
    </div>
  </header>

  <div class="abs hero" role="img" aria-label="Foto: gerollte bunte Stoffballen auf einem Marktstand"></div>
  <div class="abs hero-shade"></div>
  <div class="abs hero-dots"><i></i><i></i><i></i></div>
  <h1 class="abs hero-title">Willkommen bei Palmtuche - Sonnenfaden</h1>
  <p class="abs hero-text">Ich biete derzeit auf dem Marktreigen Nord deutschlandweit meine Stoffe an.</p>
  <div class="abs btn hero-btn">Zum Shop</div>

  <section class="abs features">
    <div class="abs feature" style="left:135px">
      <svg viewBox="0 0 44 40"><path d="M8 22v-6a14 14 0 0 1 28 0v6"/><rect x="5" y="20" width="6" height="10" rx="2"/><rect x="33" y="20" width="6" height="10" rx="2"/><rect x="14" y="14" width="16" height="11" rx="3"/><path d="M18 20h1M22 20h1M26 20h1"/></svg>
      <span>Kostenlose Beratung<br>von Experten</span>
    </div>
    <div class="abs feature" style="left:415px">
      <svg viewBox="0 0 44 40"><path d="M8 12h20v16H8zM28 18h7l5 5v5H28"/><circle cx="14" cy="30" r="3"/><circle cx="34" cy="30" r="3"/><path d="M2 18h6M4 23h4"/></svg>
      <span>Kostenlose Lieferung<br>in ganz German</span>
    </div>
    <div class="abs feature" style="left:708px">
      <svg viewBox="0 0 44 40"><rect x="4" y="8" width="26" height="15" rx="1"/><circle cx="17" cy="15.5" r="4"/><path d="M14 30l8-4h10l8 4v6H14z"/></svg>
      <span>100 Tage<br>Widerrufsrecht</span>
    </div>
    <div class="abs feature" style="left:966px">
      <svg viewBox="0 0 44 40"><path d="M14 6l8-2 8 4-2 6 4 6-4 6 2 8-10 2-6-4 2-8-4-6 4-6z"/></svg>
      <span>Made in<br>Germany</span>
    </div>
  </section>

  <h2 class="abs section-title">Eleganz kommt nie aus der Mode</h2>
  <div class="abs swatch" style="left:135px"><div class="dot" role="img" aria-label="Stoffmuster Gobelin" style="background:radial-gradient(circle,#b79a6a,#8a6a3e)"></div><p>Gobelin</p></div>
  <div class="abs swatch" style="left:301px"><div class="dot" role="img" aria-label="Stoffmuster Canvas" style="background:#e9e6df"></div><p>Canvas</p></div>
  <div class="abs swatch" style="left:467px"><div class="dot" role="img" aria-label="Stoffmuster Linen" style="background:#e3dfda"></div><p>Linen</p></div>
  <div class="abs swatch" style="left:633px"><div class="dot" role="img" aria-label="Stoffmuster Sweat" style="background:#f3f3f3"></div><p>Sweat</p></div>
  <div class="abs swatch" style="left:799px"><div class="dot" role="img" aria-label="Stoffmuster Jersey" style="background:radial-gradient(circle,#ececef,#c9c9cf)"></div><p>Jersey</p></div>
  <div class="abs swatch" style="left:965px"><div class="dot" role="img" aria-label="Stoffmuster Musselin" style="background:#e2b2a7"></div><p>Musselin</p></div>
  <div class="abs btn more-btn">Mehr Enfahren</div>

  <div class="abs banner" style="left:0;background:linear-gradient(160deg,#d9a21d 0%,#e06a2a 40%,#c83a2a 70%,#2b6a72 100%)" role="img" aria-label="Foto: gefaltete Musselinstoffe in Orange, Gelb und Petrol mit Zertifikatskarte">
    <div class="abs banner-label" style="left:127px">Bio Musselin 100% Baumwolle</div>
  </div>
  <div class="abs banner" style="left:600px;background:linear-gradient(90deg,#3a9ad0 0%,#4b7fd0 25%,#c9bd88 45%,#a8734f 60%,#4a2430 78%,#d82a3a 100%)" role="img" aria-label="Foto: Leinenstoffrollen in Blau, Beige, Braun und Rot">
    <div class="abs banner-label" style="left:181px">100% Linen Washed</div>
  </div>

  <div class="abs product" style="left:135px">
    <div class="shot" role="img" aria-label="Produktfoto: gelb-weiß gestreifter Stoff" style="background:linear-gradient(160deg,#fff 0%,#e5a53a 35%,#d98d24 70%,#fff 100%)"></div>
    <p class="tag">New Color</p><h3>Lorem ipsum dolor sit amet, consectetur</h3><p class="price">40.59 € - 50 € <small>/ Kg</small></p>
  </div>
  <div class="abs product" style="left:373px">
    <div class="shot" role="img" aria-label="Produktfoto: gefaltete Stoffe in Rot, Gelb und Blau" style="background:linear-gradient(135deg,#e07a4d 0%,#d84a50 30%,#e2c24a 50%,#6f9aa3 75%,#efe7dc 100%)"></div>
    <p class="tag">New Color</p><h3>Lorem ipsum dolor sit amet, consecte</h3><p class="price">40.59 € - 50 € <small>/ Kg</small></p>
  </div>
  <div class="abs product" style="left:611px">
    <div class="shot" role="img" aria-label="Produktfoto: gefalteter weißer Stoff" style="background:linear-gradient(160deg,#fff 0%,#eef0f6 50%,#fff 100%)"></div>
    <p class="tag">New Color</p><h3>Lorem ipsum dolor sit amet, consectetur</h3><p class="price">40.59 € - 50 € <small>/ Kg</small></p>
  </div>
  <div class="abs product" style="left:848px">
    <div class="shot" role="img" aria-label="Produktfoto: gefaltete Stoffe in Rot, Gelb und Blau" style="background:linear-gradient(135deg,#e07a4d 0%,#d84a50 30%,#e2c24a 50%,#6f9aa3 75%,#efe7dc 100%)"></div>
    <p class="tag">New Color</p><h3>Lorem ipsum dolor sit amet, consectetur</h3><p class="price">40.59 € - 50 € <small>/ Kg</small></p>
  </div>

  <h2 class="abs about-title">Uber Üns</h2>
  <p class="abs about-text">Lorem ipsum dolor sit amet, consectetur adipiscing elit. Adipiscing tincidunt orci a ipsum pellentesque eget. Quisque at dignissim metus turpis. Sed eget lorem arcu dui, viverra non commodo sed. Feugiat sed interdum nunc nunc ut vitae, odio eget. Nisl, lacus gravida mauris quis amet aliquet hendrerit integer tincidunt. Aenean egestas sit leo lobortis cras imperdiet at gravida. A ipsum sit felis malesuada ac.</p>
  <div class="abs about-photo" role="img" aria-label="Foto: gestapelte Stoffe in Orange, Rot, Gelb, Rosa und Petrol"></div>

  <footer class="abs footer">
    <div class="abs f-col" style="left:135px">
      <div class="f-brand"><b>Palmtuche</b> - Sonnenfaden</div>
      <p class="f-hot">Unsere Hotline hilft Ihnen gerne:</p>
      <p class="f-phone"><svg width="14" height="14" viewBox="0 0 14 14" fill="#fff"><path d="M3 1l2 3-1 2c1 2 2 3 4 4l2-1 3 2-1 2C6 13 1 8 1 2z"/></svg>04412 - 70218</p>
      <p class="f-hours">Mo-Fr, 10:00 - 17:00 Uhr</p>
      <div class="social"><span><i></i>Runde</span><span><i></i>Pinnbrett</span><span><i></i>Bildzeit</span></div>
    </div>
    <div class="abs f-col" style="left:462px">
      <p class="f-head">SERVICE</p>
      <p class="f-list">Hilfe/FAQ<br>Versand<br>Zahlung</p>
    </div>
    <div class="abs f-col" style="left:659px">
      <p class="f-head">UNTERNEHMEN</p>
      <p class="f-list">Impressum<br>AGB<br>Datenschutz</p>
    </div>
    <div class="abs f-col" style="left:899px">
      <p class="f-head">ZAHLUNG/VERSAND</p>
      <div class="pay"><span>Zahlfix</span><span>Kartenring</span><span>Mondkarte</span><span>Ratenwerk</span><span>Euroeinzug</span></div>
      <div class="pay-rule"></div>
      <div class="pay" style="margin-top:0"><span>Paketblitz</span><span>Kurierpunkt</span></div>
    </div>
  </footer>

</div>
</body>
</html>
```